Velbrook Leaf is a bridge for the people who drink tea to connect with the people who make the tea and the environment in which it is grown.

As a start-up, Velbrook Leaf needs to establish a fluently persuasive brand image that articulates its unique mission to the up-market tea drinker.

Our passion for high quality tea and our respect for people are boundless. But our budget is shoe-string. Still, we will allocate a disproportionate amount to evolving a brand; including logo, labeling, and packaging, and hope this initial effort will lead to a long-term relationship with a designer. The Velbrook label, as a component of the brand, must deny the commodity image of tea by broadcasting the uniquely flavorful, healthful, and relaxing experience of drinking tea.

The logo is an image of a liquor pouring from above into a stylized outline of a cup and gracefully folding over on itself within the cup. The image is an echo of video clips that will be featured on the Product page of the ecommerce site. Our initial thought is for the liquor and cup to be white on a rich blue background. But you may have a better idea.

The label must fit a seamless tin canister 4" in diameter; 2" high with a "window" in the lid. There are really three distinct parts to the label: a) wrap-around for the body of the tin; b) a distinct piece to be applied underneath the tin; and c) security strip (s) that connect the lid and the bottom of the tin. The wrap-around must include the following components: the logo, the brand name 'Velbrook Leaf', the name of the specific tea and space for the following characteristics of the tea: Tea / Garden Name, Harvest Date, Tasting Notes, Weight, Location, and Caffeine content. The piece to be affixed underneath the tin should accommodate Ingredients, Brewing Instructions, and contact details for Velbrook Leaf. The security strip(s) should be an integral part of the overall visual.

The color scheme should be expandable, i.e.; different colors for different teas.
We are thinking about rich and bold colors. But am eager to see what inspires you!

A very rough proto-type is captured in the attached files.

Target Market(s)

Ages 25 to 45 in densely populated areas of the U.S. and Canada will an above average house-hold income and an interest in what they eat / drink.

Industry/Entity Type

Environment

Requirements
Must have
• 1. Three separate pieces: 1) wrap around for the body of the tin; 2) piece to be affixed to the bottom of the body of the tin; 3) security strip (s). A word about strips: am unsure about one vs two because, two will add to overhead and processing while one will block the view of the contents. Maybe you know how to resolve.
2. clean, crisp lines
3. uncluttered
Nice to have
• 1. a color scheme to accommodate up to 30 different teas. Do not fall into the trap of incorporating the color green on the label for a 'green tea' and yellow for a lemon flavored tea. That approach is limited and has been overdone.
2. a color scheme that, as it expands to accommodate 30 teas, also is anchored by a brand color set. In other words, all labels include a recognizable color set.
3. express the level of caffeine via a gauge or metric
Should not have
• photo images,

```html
<!DOCTYPE html>
<html lang="en">
<head>
<meta charset="utf-8">
<title>Velbrook Leaf – Mandarin Tin Label Set</title>
<link href="https://fonts.googleapis.com/css2?family=Oswald:wght@400;500;600&family=Roboto+Condensed:wght@400;700&family=Archivo+Narrow:wght@400;700&display=swap" rel="stylesheet">
<style>
  :root{
    --ink:#000000;
    --paper:#ffffff;
    --title-grey:#e4e4e4;
    --band-light:#ffffff;
    --band-shade:#c9c9c9;
    --tea-red:#b0232c;
    --tea-red-deep:#5e0f15;
    --tea-red-mid:#8a1a22;
    --caption:#b9b9b9;
    --body-text:#d8d8d8;
  }
  *{margin:0;padding:0;box-sizing:border-box}
  html,body{width:1200px;height:806px;overflow:hidden;background:var(--paper)}
  .canvas{position:relative;width:1200px;height:806px;background:var(--paper);font-family:"Roboto Condensed",Arial,sans-serif}

  /* Wrap-around label */
  .wrap-label{position:absolute;left:6px;top:15px;width:1188px;height:337px}
  .wrap-label svg{position:absolute;inset:0}
  .wrap-title{position:absolute;left:0;right:0;top:22px;text-align:center;font-family:"Oswald",sans-serif;font-weight:600;font-size:52px;letter-spacing:1px;color:var(--title-grey);line-height:1}
  .badge-name{position:absolute;left:524px;top:172px;width:140px;text-align:center;font-family:"Oswald",sans-serif;font-weight:500;font-size:17px;color:var(--paper);line-height:1}
  .tea-name{position:absolute;left:0;right:0;top:276px;text-align:center;font-family:"Oswald",sans-serif;font-weight:500;font-size:21px;color:var(--paper);line-height:1.3}

  /* Base label */
  .base-label{position:absolute;left:151px;top:367px;width:420px;height:420px}
  .base-label svg{position:absolute;inset:0}
  .base-name{position:absolute;left:0;right:0;top:56px;text-align:center;font-family:"Oswald",sans-serif;font-weight:500;font-size:15px;color:var(--paper)}
  .nutrition{position:absolute;left:55px;top:115px;width:115px;height:148px;background:var(--paper);color:var(--ink);font-family:"Archivo Narrow",Arial,sans-serif;font-size:5.4px;line-height:1.25;padding:2px 3px}
  .nutrition h3{font-family:"Archivo Narrow",Arial,sans-serif;font-weight:700;font-size:12px;line-height:1;border-bottom:0.6px solid var(--ink)}
  .nutrition .row{display:flex;justify-content:space-between;border-bottom:0.5px solid var(--ink)}
  .nutrition .thick{border-bottom:3px solid var(--ink)}
  .nutrition .mid{border-bottom:1.5px solid var(--ink)}
  .nutrition .sub{padding-left:6px}
  .nutrition b{font-weight:700}
  .nutrition .note{font-size:4.4px;line-height:1.2;padding-top:1px}
  .base-title{position:absolute;left:179px;top:114px;font-family:"Oswald",sans-serif;font-weight:600;font-size:29px;color:var(--paper);line-height:1;letter-spacing:.3px}
  .base-copy{position:absolute;left:179px;top:154px;width:178px;font-family:"Roboto Condensed",sans-serif;font-size:10.6px;line-height:1.42;color:var(--body-text);text-align:justify}
  .contact-icons{position:absolute;left:174px;top:302px;display:flex;gap:20px}
  .base-footer{position:absolute;left:70px;right:70px;top:336px;text-align:center;font-family:"Roboto Condensed",sans-serif;font-size:10.6px;line-height:1.32;color:var(--body-text)}

  /* Security strip */
  .security-strip{position:absolute;left:669px;top:439px;width:113px;height:282px;background:linear-gradient(90deg,var(--tea-red-deep),var(--tea-red) 30%,var(--tea-red-mid) 55%,var(--tea-red) 80%,var(--tea-red-deep))}
  .strip-name{position:absolute;left:0;right:0;top:131px;text-align:center;font-family:"Oswald",sans-serif;font-weight:500;font-size:15px;color:var(--paper)}
  .strip-caption{position:absolute;left:669px;top:726px;font-family:"Roboto Condensed",sans-serif;font-size:14px;color:var(--caption)}
</style>
</head>
<body>
<main class="canvas">

  <section class="wrap-label" aria-label="Wrap-around body label">
    <svg width="1188" height="337" viewBox="0 0 1188 337">
      <defs>
        <linearGradient id="band" x1="0" y1="0" x2="0" y2="1">
          <stop offset="0" stop-color="var(--band-light)"/>
          <stop offset="1" stop-color="var(--band-shade)"/>
        </linearGradient>
        <linearGradient id="redField" x1="0" y1="0" x2="0" y2="1">
          <stop offset="0" stop-color="#3e0a0e"/>
          <stop offset=".5" stop-color="var(--tea-red-mid)"/>
          <stop offset="1" stop-color="var(--tea-red)"/>
        </linearGradient>
      </defs>
      <rect class="wrap-black" width="1188" height="337" fill="var(--ink)"/>
      <path class="wrap-band" d="M0,250 Q594,80 1188,250 L1188,337 L0,337 Z" fill="url(#band)"/>
      <path class="wrap-field" role="img" aria-label="Red bamboo stalk texture" d="M0,268 Q594,112 1188,268 L1188,337 L0,337 Z" fill="url(#redField)"/>
      <circle class="brand-badge" cx="594" cy="182" r="66" fill="var(--tea-red)" stroke="#eeeeee" stroke-width="12"/>
    </svg>
    <h1 class="wrap-title">VELBROOK LEAF</h1>
    <div class="badge-name">Velbrook Leaf</div>
    <p class="tea-name">MANDARIN<br>500 G</p>
  </section>

  <section class="base-label" aria-label="Base label">
    <svg width="420" height="420" viewBox="0 0 420 420">
      <defs>
        <radialGradient id="rim" cx=".5" cy=".5" r=".5">
          <stop offset=".82" stop-color="var(--tea-red-deep)"/>
          <stop offset=".92" stop-color="var(--tea-red)"/>
          <stop offset="1" stop-color="var(--tea-red-mid)"/>
        </radialGradient>
      </defs>
      <circle role="img" aria-label="Red bamboo stalk texture" cx="210" cy="210" r="210" fill="url(#rim)"/>
      <circle cx="210" cy="206" r="184" fill="var(--ink)"/>
    </svg>
    <div class="base-name">Velbrook Leaf</div>

    <div class="nutrition">
      <h3>Nutrition Facts</h3>
      <div>Serving Size 1 Tea Bag 2g (2 g)</div>
      <div class="thick">Servings per container 30</div>
      <div class="row"><b>Amount Per Serving</b></div>
      <div class="row mid"><span><b>Calories</b> 3</span><span>Calories from Fat 0</span></div>
      <div class="row" style="justify-content:flex-end"><b>% Daily Value*</b></div>
      <div class="row"><span><b>Total Fat</b> 0g</span><span>0%</span></div>
      <div class="row sub"><span>Saturated Fat</span><span>0%</span></div>
      <div class="row sub"><span>Trans Fat</span><span></span></div>
      <div class="row"><span><b>Cholesterol</b></span><span>0%</span></div>
      <div class="row"><span><b>Sodium</b> 1mg</span><span>0%</span></div>
      <div class="row"><span><b>Total Carbohydrate</b></span><span>0%</span></div>
      <div class="row sub"><span>Dietary Fiber</span><span>0%</span></div>
      <div class="row sub"><span>Sugars</span><span></span></div>
      <div class="row thick"><span><b>Protein</b></span><span></span></div>
      <div class="row"><span>Vitamin A 17% • Vitamin C</span><span>1%</span></div>
      <div class="row mid"><span>Calcium 5% • Iron</span><span>5%</span></div>
      <div class="note">*Percent Daily Values are based on a 2,000 calorie diet. Your daily values may vary with your calorie needs.</div>
    </div>

    <h2 class="base-title">VELBROOK LEAF</h2>
    <p class="base-copy">Lorem ipsum dolor sit amet, consectetur adipiscing elit. Duis condimentum non massa nec vulputate. Aliquam viverra quam id sapien aliquam, porttitor sollicitudin orci dapibus. In eget tempus nulla. In hac habitasse platea dictumst. Suspendisse porta malesuada tortor, at tincidunt purus malesuada id.</p>

    <div class="contact-icons">
      <svg class="icon-phone" width="24" height="20" viewBox="0 0 24 20" aria-label="Phone">
        <path d="M2,6 Q12,-1 22,6 L20,9 L16,8 L16,5 Q12,4 8,5 L8,8 L4,9 Z" fill="var(--paper)"/>
        <path d="M6,10 L18,10 L21,19 L3,19 Z" fill="var(--paper)"/>
        <circle cx="12" cy="14" r="3" fill="var(--ink)"/>
      </svg>
      <svg class="icon-mail" width="24" height="18" viewBox="0 0 24 18" aria-label="Email">
        <rect x="1" y="1" width="22" height="16" fill="none" stroke="var(--paper)" stroke-width="2"/>
        <path d="M1,1 L12,10 L23,1" fill="none" stroke="var(--paper)" stroke-width="2"/>
      </svg>
    </div>

    <p class="base-footer">Vivamus scelerisque augue felis, non eleifend dui commodo sed. Maecenas feugiat, nibh sed vulputate porttitor, nisi quam aliquam risus,</p>
  </section>

  <section class="security-strip" role="img" aria-label="Security strip with red bamboo stalk texture">
    <div class="strip-name">Velbrook Leaf</div>
  </section>
  <p class="strip-caption">security strip</p>

</main>
</body>
</html>
```